tilebarnowl.net needs a cool website!

I need a website designed for a commercial flooring maintenance company based in Texas. We will be providing services like carpet shampooing, burnishing, resurfacing and power washing. It needs to be cool and trendy.

I’ll need 10-20 pages. I need help deciding on the style and color palette. We will need great stock pictures of different flooring types and you will need to photo shop our logo on imaginary cars or storefronts.

Please have similar experience and an open mind. I’m looking for a partnership and someone to turn to for future projects and upkeep.

The domain is currently hosted on Wix. You will need the ability to develop and code it there.

Target Market(s)

Commercial businesses and properties

Industry/Entity Type

Floor care

Coding

Coded - Design and coding required

Number of Pages Required

5+ page

Requirements
Must have
• Great pictures of different types of floors.

```html
<!DOCTYPE html>
<html lang="en">
<head>
<meta charset="utf-8">
<title>tilebarnowl — Commercial Floor Care</title>
<link rel="stylesheet" href="https://fonts.googleapis.com/css2?family=Inter:wght@400;500;600&display=swap">
<style>
:root{
  --canvas:#fbfbfa;
  --white:#ffffff;
  --ink:#1d1d1d;
  --muted:#444444;
  --green:#8cc63f;
  --green-dark:#2f4a1c;
  --green-bar:#5d8a2c;
  --soft:#f4f4f4;
  --rule:#d6d6d6;
}
*{margin:0;padding:0;box-sizing:border-box}
html,body{width:1200px;height:2708px;overflow:hidden;background:var(--canvas);font-family:"Inter",Arial,sans-serif;color:var(--ink)}
.page{position:absolute;left:148px;top:152px;width:897px;background:var(--white);box-shadow:0 0 60px rgba(140,198,63,.12),0 0 40px rgba(0,0,0,.05)}
section,header,footer{position:relative;width:100%}
.abs{position:absolute}

/* nav */
.site-nav{height:42px}
.brand{position:absolute;left:24px;top:13px;font-size:12px;color:var(--ink);font-weight:400;display:flex;align-items:center;gap:5px}
.brand .dot{width:9px;height:9px;border-radius:50%;background:var(--ink)}
.nav-links{position:absolute;right:136px;top:14px;display:flex;gap:17px;font-size:9px}
.nav-links .current{text-decoration:underline}
.btn-contact{position:absolute;left:781px;top:8px;width:83px;height:24px;background:var(--green);color:var(--green-dark);font-size:8px;font-weight:600;display:flex;align-items:center;justify-content:center;letter-spacing:.3px}

/* hero */
.hero{height:376px;overflow:hidden}
.hero-photo{position:absolute;inset:0;background:linear-gradient(90deg,#2c2a28 0%,#4b4036 30%,#9c7551 55%,#c59a6b 75%,#b88b5e 100%)}
.hero-title{left:51px;top:155px;font-size:37px;line-height:38px;color:var(--white);font-weight:400;letter-spacing:-1.8px}
.hero-text{left:51px;top:241px;width:320px;font-size:8.5px;line-height:12px;color:var(--white)}
.hero-cta{left:51px;top:302px;display:flex;align-items:center;gap:11px;color:var(--white);font-size:8px}
.sq{width:28px;height:28px;display:flex;align-items:center;justify-content:center}
.sq.green{background:var(--green)}
.sq.dark{background:var(--green-dark)}

/* shared heading */
.eyebrow{display:flex;align-items:center;gap:6px;font-size:7.5px;letter-spacing:.2px;text-transform:uppercase}
.eyebrow i{width:8px;height:8px;background:var(--ink);clip-path:polygon(0 0,60% 0,100% 50%,60% 100%,0 100%)}
.h2{font-size:28px;font-weight:400;letter-spacing:-.8px;color:var(--ink)}

/* services */
.services{height:480px}
.services .eyebrow{left:34px;top:45px}
.services .h2{left:34px;top:69px}
.services .lede{left:34px;top:120px;width:520px;font-size:8.5px;line-height:12.5px}
.learn{left:34px;top:163px;display:flex;align-items:center;gap:11px;font-size:7.5px}
.cards{left:34px;top:236px;display:flex;gap:23px}
.card{width:190px}
.card .ph{height:107px}
.card h3{font-size:13.5px;font-weight:400;margin-top:8px;letter-spacing:-.3px}
.card p{font-size:7.5px;line-height:10.5px;color:var(--muted)}
.ph-carpet{background:linear-gradient(135deg,#cbb899,#e8e0d0 50%,#3d9ab8)}
.ph-burnish{background:linear-gradient(180deg,#6d6a66,#9a9896 45%,#c5622a 70%,#8e3d16)}
.ph-resurface{background:linear-gradient(180deg,#c9915c,#d9a877 55%,#b77c48)}
.ph-wash{background:linear-gradient(90deg,#3c3a36,#d6c3a8 45%,#6c8a45 80%,#4e6a36)}

/* about */
.about{height:437px;overflow:hidden}
.about-photo{position:absolute;inset:0;background:linear-gradient(90deg,#c9ceb0 0%,#c4c8a8 45%,#9ea27c 52%,#a9a785 75%,#b8b392 100%)}
.about .eyebrow{left:62px;top:46px;color:var(--white)}
.about .eyebrow i{background:var(--white)}
.about .h2{left:62px;top:67px;color:var(--white)}
.about .lede{left:62px;top:106px;width:360px;font-size:12.5px;line-height:18px;color:var(--white)}
.about-cta{left:62px;top:200px;display:flex;align-items:center;gap:11px;font-size:7.5px;color:var(--white)}

/* partners */
.partners{height:220px;background:var(--soft);display:flex;align-items:center;justify-content:space-around;padding:0 50px}
.partners span{font-size:22px;color:var(--ink);font-weight:400;letter-spacing:-.5px}

/* projects */
.projects{height:458px}
.projects .eyebrow{left:34px;top:46px}
.projects .h2{left:34px;top:70px}
.more{left:34px;top:135px;height:28px;border-left:1px solid #eee;padding-left:39px;display:flex;align-items:center;font-size:7.5px}
.gallery{left:34px;top:190px;display:flex;gap:19px}
.gallery div{width:238px;height:178px}
.g1{background:linear-gradient(180deg,#7c5a3e,#d9cdb9 45%,#a35e32 80%,#6e3b1d)}
.g2{background:linear-gradient(180deg,#e9e9e7,#f4f4f2 55%,#a86e3e 80%,#7a4a24)}
.g3{background:linear-gradient(160deg,#eef3f8,#bcd1e8 45%,#8b95a3 80%,#6f7885)}

/* band */
.band{height:150px;background:var(--green)}
.band .bar{left:408px;top:112px;width:83px;height:5px;background:var(--green-bar)}

/* footer */
.site-footer{height:226px;background:var(--soft)}
.site-footer .brand{left:34px;top:50px;font-size:15px}
.col{top:46px;font-size:8px;line-height:11px}
.col h4{font-size:8px;font-weight:400;text-transform:uppercase;margin-bottom:14px}
.col li{list-style:none;margin-bottom:10.5px}
.col.office li{margin-bottom:15px}
.col.office{left:258px}
.col.nav{left:491px}
.col.follow{left:669px}
.foot-rule{left:34px;right:34px;top:175px;height:1px;background:var(--rule)}
.copy{left:34px;top:192px;font-size:8px}
.legal{right:34px;top:192px;font-size:8px;display:flex;gap:31px}
</style>
</head>
<body>
<div class="page">

  <header class="site-nav">
    <div class="brand"><span class="dot"></span>tilebarnowl</div>
    <nav class="nav-links"><span class="current">Home</span><span>Services</span><span>Projects</span><span>About us</span></nav>
    <div class="btn-contact">CONTACT</div>
  </header>

  <section class="hero">
    <div class="hero-photo" role="img" aria-label="Hands laying light oak laminate floor planks"></div>
    <h1 class="abs hero-title">Transform Your Floors.<br>Elevate Your Space.</h1>
    <p class="abs hero-text">We provide expert commercial flooring maintenance services across Texas, ensuring your floors look as good as new.</p>
    <div class="abs hero-cta">
      <span class="sq green"><svg width="12" height="10" viewBox="0 0 12 10"><path d="M0 5h10M6 1l4 4-4 4" stroke="#1d1d1d" stroke-width="1.3" fill="none"/></svg></span>
      Get a Free Quote
    </div>
  </section>

  <section class="services">
    <div class="abs eyebrow"><i></i>Our Services</div>
    <h2 class="abs h2">Diverse Services tailored to your flooring needs</h2>
    <p class="abs lede">With years of experience in floor care, we specialize in making your floors last longer and look their best. Our team provides professional carpet shampooing, burnishing, resurfacing, and power washing.</p>
    <div class="abs learn">
      <span class="sq dark"><svg width="12" height="10" viewBox="0 0 12 10"><path d="M0 5h10M6 1l4 4-4 4" stroke="#fff" stroke-width="1.3" fill="none"/></svg></span>
      LEARN MORE
    </div>
    <div class="abs cards">
      <article class="card"><div class="ph ph-carpet" role="img" aria-label="Carpet shampoo machine cleaning a beige carpet"></div><h3>Carpet Shampooing</h3><p>Revitalize your carpets with deep cleaning for a fresh, professional look.</p></article>
      <article class="card"><div class="ph ph-burnish" role="img" aria-label="Floor burnishing machine on a glossy floor"></div><h3>Burnishing</h3><p>Restore the shine of your floors with expert burnishing services for a smooth, glossy finish.</p></article>
      <article class="card"><div class="ph ph-resurface" role="img" aria-label="Flat mop on a wooden floor"></div><h3>Resurfacing</h3><p>Repair and renew damaged floors, giving them a brand-new appearance.</p></article>
      <article class="card"><div class="ph ph-wash" role="img" aria-label="Pressure washer spraying an outdoor surface"></div><h3>Power Washing</h3><p>Remove dirt, grime, and buildup from your exterior surfaces with our powerful pressure washing service.</p></article>
    </div>
  </section>

  <section class="about">
    <div class="about-photo" role="img" aria-label="Installer rolling out carpet over a herringbone wood floor"></div>
    <div class="abs eyebrow"><i></i>About</div>
    <h2 class="abs h2">About Tilebarnowl</h2>
    <p class="abs lede">With years of experience in floor care, we specialize in making your floors last longer and look their best. Our team provides professional carpet shampooing, burnishing, resurfacing, and power washing.</p>
    <div class="abs about-cta">
      <span class="sq green"><svg width="12" height="10" viewBox="0 0 12 10"><path d="M0 5h10M6 1l4 4-4 4" stroke="#1d1d1d" stroke-width="1.3" fill="none"/></svg></span>
      Schedule a Service
    </div>
  </section>

  <section class="partners">
    <span>Lumora</span><span>Vantrel</span><span>Quadrix</span><span>NORTEX</span><span>Harbor</span>
  </section>

  <section class="projects">
    <div class="abs eyebrow"><i></i>Recent Projects</div>
    <h2 class="abs h2">See Our Work</h2>
    <div class="abs more">MORE PROJECTS</div>
    <div class="abs gallery">
      <div class="g1" role="img" aria-label="Loft room with brick walls and polished wood floor"></div>
      <div class="g2" role="img" aria-label="Bright attic room with hardwood floor"></div>
      <div class="g3" role="img" aria-label="White courtyard with stone paving"></div>
    </div>
  </section>

  <section class="band"><div class="abs bar"></div></section>

  <footer class="site-footer">
    <div class="brand"><span class="dot"></span>tilebarnowl</div>
    <div class="abs col office"><h4>Head Office</h4><ul><li>Texas, TX 7520</li><li>123-555-0142</li><li>info@tilebarnowl.net</li></ul></div>
    <div class="abs col nav"><h4>Navigation</h4><ul><li>Services</li><li>Projects</li><li>About us</li><li>Contact</li></ul></div>
    <div class="abs col follow"><h4>Follow Us</h4><ul><li>Chatter</li><li>Pictura</li><li>Linkwise</li></ul></div>
    <div class="abs foot-rule"></div>
    <div class="abs copy">© 2024 by Tilebarnowl Inc.</div>
    <div class="abs legal"><span>Terms &amp; Conditions</span><span>Privacy Policy</span></div>
  </footer>

</div>
</body>
</html>
```